Vostrel LTB Book Cover Design: Book 1 of 4

Designers must not submit more than 1 design. Submission of multiple designs will result in disqualification.

Designer must be highly experienced with properly designing and formatting Vostrel LTB book covers. The winner of this contest will receive three more covers to do. This project is for one of four books in a series. I want the same designer to do all four books because they are in a series and need to look the same. Attached are the directions and files.

Target Market(s)

see attachments

Industry/Entity Type

see attachments

Requirements
Must have
• see attachments
Nice to have
• see attachments
Should not have
• see attachments

```html
<!DOCTYPE html>
<html lang="en">
<head>
<meta charset="utf-8">
<title>How to Become a Real Estate Millionaire – Book Cover</title>
<link rel="stylesheet" href="https://fonts.googleapis.com/css2?family=Bebas+Neue&family=Oswald:wght@500;600&family=Roboto+Condensed:wght@400;500&display=swap">
<style>
  :root {
    --page-bg: #e4e1e2;
    --navy: #0f1a2e;
    --navy-deep: #0a1322;
    --white: #ffffff;
    --ink: #0f1a2e;
    --accent-blue: #5f93cf;
    --divider: rgba(160, 185, 220, 0.55);
    --dusk-blue: #1c3152;
    --dusk-orange: #b0765a;
    --water: #142640;
  }
  * { margin: 0; padding: 0; box-sizing: border-box; }
  html, body {
    width: 1200px; height: 1200px; overflow: hidden;
    background: var(--page-bg);
  }
  .cover {
    position: absolute; left: 250px; top: 56px;
    width: 700px; height: 1088px;
    background: var(--navy);
    overflow: hidden;
    color: var(--white);
    text-align: center;
  }
  .cover-photo {
    position: absolute; left: 0; right: 0; top: 640px; bottom: 0;
    background: linear-gradient(180deg,
      var(--navy) 0%,
      var(--dusk-blue) 22%,
      var(--dusk-orange) 42%,
      var(--dusk-blue) 52%,
      var(--water) 70%,
      var(--navy-deep) 100%);
  }
  .tagline {
    position: absolute; top: 46px; left: 0; right: 0;
    font: 500 20px/1 "Oswald", sans-serif;
    letter-spacing: 3.5px;
  }
  .title-lead {
    position: absolute; top: 92px; left: 0; right: 0;
    font: 600 54px/1 "Oswald", sans-serif;
    letter-spacing: 3px;
  }
  .title-main {
    position: absolute; left: 0; right: 0;
    font: 400 152px/1 "Bebas Neue", sans-serif;
    letter-spacing: 1px;
  }
  .title-main.line-1 { top: 160px; }
  .title-main.line-2 { top: 288px; }
  .pillars-banner {
    position: absolute; left: 84px; top: 425px; width: 569px; height: 52px;
    background: var(--white); color: var(--ink);
    border-radius: 10px;
    font: 600 34px/52px "Oswald", sans-serif;
    letter-spacing: 4px;
  }
  .pillar {
    position: absolute; top: 496px; width: 160px; margin-left: -80px;
  }
  .pillar-icon {
    width: 71px; height: 71px; margin: 0 auto;
    border-radius: 50%; background: var(--white);
    display: flex; align-items: center; justify-content: center;
  }
  .pillar-name {
    margin-top: 12px;
    font: 500 20px/1 "Oswald", sans-serif;
    letter-spacing: 0.5px;
  }
  .pillar-text {
    margin-top: 6px;
    font: 400 16.5px/1.3 "Roboto Condensed", sans-serif;
  }
  .pillar-divider {
    position: absolute; top: 498px; width: 1px; height: 148px;
    background: var(--divider);
  }
  .subtitle-box {
    position: absolute; left: 123px; top: 873px; width: 438px; height: 55px;
    background: var(--white); color: var(--ink);
    border-radius: 6px;
    font: 500 17.5px/24px "Oswald", sans-serif;
    letter-spacing: 0.6px;
    padding-top: 4px;
  }
  .author {
    position: absolute; top: 948px; left: 0; right: 0;
    font: 600 66px/1 "Oswald", sans-serif;
    letter-spacing: 3px;
  }
  .author-roles {
    position: absolute; top: 1022px; left: 0; right: 0;
    font: 500 17.5px/1 "Oswald", sans-serif;
    letter-spacing: 1.5px;
    color: var(--accent-blue);
  }
</style>
</head>
<body>
  <main class="cover">
    <div class="cover-photo" role="img" aria-label="Photograph of a lit suspension bridge over water at dusk, with rocks in the foreground"></div>

    <p class="tagline">BUILDING WEALTH ONE HOUSE AT A TIME</p>
    <h1>
      <span class="title-lead">HOW TO BECOME A</span>
      <span class="title-main line-1">REAL ESTATE</span>
      <span class="title-main line-2">MILLIONAIRE</span>
    </h1>
    <p class="pillars-banner">THE 4 PILLARS OF SUCCESS</p>

    <div class="pillar" style="left:122px">
      <div class="pillar-icon">
        <svg width="44" height="44" viewBox="0 0 44 44" aria-hidden="true">
          <circle cx="22" cy="22" r="16" fill="var(--navy)"/>
          <text x="22" y="29" text-anchor="middle" font-family="Oswald, sans-serif" font-size="20" font-weight="600" fill="#fff">$</text>
        </svg>
      </div>
      <p class="pillar-name">MINDSET</p>
      <p class="pillar-text">Think Like<br>a Millionaire</p>
    </div>
    <span class="pillar-divider" style="left:198px"></span>

    <div class="pillar" style="left:275px">
      <div class="pillar-icon">
        <svg width="44" height="44" viewBox="0 0 44 44" aria-hidden="true">
          <path d="M6 12 Q14 9 21 13 V34 Q14 30 6 33 Z" fill="none" stroke="var(--navy)" stroke-width="3" stroke-linejoin="round"/>
          <path d="M38 12 Q30 9 23 13 V34 Q30 30 38 33 Z" fill="none" stroke="var(--navy)" stroke-width="3" stroke-linejoin="round"/>
        </svg>
      </div>
      <p class="pillar-name">EDUCATION</p>
      <p class="pillar-text">Learn the<br>Right Skills</p>
    </div>
    <span class="pillar-divider" style="left:356px"></span>

    <div class="pillar" style="left:435px">
      <div class="pillar-icon">
        <svg width="46" height="44" viewBox="0 0 46 44" aria-hidden="true">
          <path d="M4 18 L14 12 L24 16 L34 12 L42 18 L34 28 L24 32 L12 28 Z" fill="var(--navy)"/>
        </svg>
      </div>
      <p class="pillar-name">PARTNERSHIPS</p>
      <p class="pillar-text">Build Powerful<br>Relationships</p>
    </div>
    <span class="pillar-divider" style="left:520px"></span>

    <div class="pillar" style="left:597px">
      <div class="pillar-icon">
        <svg width="44" height="44" viewBox="0 0 44 44" aria-hidden="true">
          <path d="M6 22 L22 8 L38 22" fill="none" stroke="var(--navy)" stroke-width="4" stroke-linejoin="round" stroke-linecap="round"/>
          <path d="M11 20 V36 H19 V27 H25 V36 H33 V20" fill="var(--navy)"/>
        </svg>
      </div>
      <p class="pillar-name">SYSTEMS</p>
      <p class="pillar-text">Create Scalable<br>Processes</p>
    </div>

    <p class="subtitle-box">A STEP-BY-STEP GUIDE TO FINANCIAL FREEDOM<br>THROUGH REAL ESTATE INVESTING</p>

    <p class="author">DANIEL R. HALE</p>
    <p class="author-roles">REAL ESTATE INVESTOR | ENTREPRENEUR | MENTOR</p>
  </main>
</body>
</html>
```